Walk Through Fire Step out, step up and into your best performance

BRIEF FOR BOOK FRONT COVER

• It needs to be iconic
• It needs to be a ‘clean’ design
• Needs to be seen on a bookshelf in an airport from 50 feet away
• No stick like figures/cartoon style or cutesy design
• The book appeals to both male and female readers
• This is a cross over book and covers a couple of genres like Martin Kessler’s book Small Steady Gains or Tessa Holm’s Quiet Mastery. So it is primarily about taking better care of yourself personally, professionally and will appeal to those in business.
• The idea that a personal enriching life feeds into an engaged performer on the job – they feed off each other leading to increased engagement, productivity and fulfillment
• The dance analogy means that you are not sitting on the sidelines of your life or business
• It is laced with inspiring real life case studies
• Positioning of the book: People facing adversity and still come through better than ever and better equipped to what comes next.
• Want a cover that would attract a Pinnacle 40 CEO to buy the book for his staff
• My name as the author should be across the bottom MIRIAM FOSTER MBA MCC
Updates

Project Deadline Extended Reason: A big thank you for all the designers who submitted a cover design and I have been spoilt for choiceI need to finalize the copy on the book cover and hence the need for an extension of time.Thanks for your understanding.Miriam Added Sunday, September 18, 2016

Target Market(s)

Professionals in the age group 25 - 55

Industry/Entity Type

Airport

Contact Information for Business Card

basic information and a very clean look

Logo Text

probably book title more important that it can be seen clearly when the size is reduced to a small size e.g. if sponsoring an event

Number of Pages Required

5+ page

Font styles to use
Sans Serif

Colors
ec1f27
f37122
abd037

Requirements
Must have
• info already provided

```html
<!DOCTYPE html>
<html lang="en">
<head>
<meta charset="UTF-8">
<title>Walk Through Fire – Front Cover</title>
<link rel="stylesheet" href="https://fonts.googleapis.com/css2?family=Anton&family=Montserrat:wght@500;800&family=Oswald:wght@500&display=swap">
<style>
  :root {
    --red: #ec1f27;
    --orange: #f37122;
    --orange-deep: #c94a12;
    --green: #abd037;
    --green-vivid: #86c440;
    --green-deep: #5f9e2c;
    --white: #ffffff;
    --backdrop: #f2f2f2;
    --figure-warm: #b5532a;
    --figure-dark: #6b2e1f;
  }
  html, body {
    margin: 0;
    width: 1200px;
    height: 1200px;
    overflow: hidden;
    background: var(--backdrop);
  }
  .canvas {
    position: relative;
    width: 1200px;
    height: 1200px;
  }
  .cover {
    position: absolute;
    left: 220px;
    top: 30px;
    width: 760px;
    height: 1140px;
    background: radial-gradient(ellipse at 50% 45%, var(--green-vivid) 0%, var(--green) 55%, var(--green-deep) 130%);
    overflow: hidden;
    box-shadow: 0 6px 24px rgba(0,0,0,0.18);
  }
  .tagline-band {
    height: 84px;
    background: var(--red);
    display: flex;
    align-items: center;
    justify-content: center;
    font-family: "Montserrat", sans-serif;
    font-weight: 500;
    font-size: 25px;
    letter-spacing: 1px;
    color: var(--white);
    text-transform: uppercase;
    white-space: nowrap;
  }
  .title {
    margin: 48px 0 0;
    text-align: center;
    font-family: "Anton", sans-serif;
    font-weight: 400;
    color: var(--orange);
    text-transform: uppercase;
    text-shadow: 3px 3px 0 var(--orange-deep);
    line-height: 0.95;
    white-space: nowrap;
  }
  .title-main {
    display: block;
    font-size: 210px;
    letter-spacing: 8px;
  }
  .title-sub {
    display: block;
    font-size: 104px;
    letter-spacing: 4px;
  }
  .subtitle {
    margin: 18px auto 0;
    width: 640px;
    padding: 10px 0;
    border-top: 2px solid rgba(255,255,255,0.8);
    border-bottom: 2px solid rgba(255,255,255,0.8);
    text-align: center;
    font-family: "Oswald", sans-serif;
    font-weight: 500;
    font-size: 22px;
    color: var(--white);
    text-transform: uppercase;
    letter-spacing: 0.5px;
    white-space: nowrap;
  }
  .dancers-illustration {
    position: absolute;
    left: 150px;
    top: 545px;
    width: 480px;
    height: 410px;
    border-radius: 28px;
    background: linear-gradient(160deg, var(--orange) 0%, var(--figure-warm) 55%, var(--figure-dark) 100%);
  }
  .author {
    position: absolute;
    left: 0;
    right: 0;
    bottom: 60px;
    margin: 0;
    text-align: center;
    font-family: "Montserrat", sans-serif;
    font-weight: 800;
    font-size: 42px;
    letter-spacing: 1px;
    color: var(--red);
    text-transform: uppercase;
    white-space: nowrap;
  }
</style>
</head>
<body>
  <main class="canvas">
    <section class="cover">
      <header class="tagline-band">Laced with inspiring real life case studies</header>
      <h1 class="title">
        <span class="title-main">Walk</span>
        <span class="title-sub">Through Fire</span>
      </h1>
      <p class="subtitle">Step out, step up and step into your best performance</p>
      <div class="dancers-illustration" role="img" aria-label="Illustration of a man and woman in vintage clothes swing dancing, casting a shadow on the floor"></div>
      <p class="author">Miriam Foster MBA MCC</p>
    </section>
  </main>
</body>
</html>
```